Local Horticulturalist needs Business card design

Meridale Gardening would like to update our existing business card and utilize our new logo (design attached)....we specialize in getting the best out of our customers yard with professional maintenance programs, expert pruning and hedging and garden restorations.
Utilizing colors from attached logo I would like a design that implies professionalism and if possible our businesses love of restoration through plants.
I also sometimes write down for my customers a start date and price on the back of my current card
Target Market(s)
Home owners
Contractors
Industry/Entity Type
Gardener
Contact Information for Business Card
Trevor Kalbrook | Horticulturalist
ph: 0452739186
meridalegard@fernpost.com
www.meridalegardening.com.au
Requirements
Must have
- crucial information easy to read
- incorporate current logo
- Horticulturalist listed preferably near name
Nice to have
- currently I write a job start date and price on the back of my current card so something that integrates this would be beneficial
Should not have
- be pretty or flowerey
- be too white or basic

```html
<!DOCTYPE html>
<html lang="en">
<head>
<meta charset="utf-8">
<title>Meridale Gardening – Business Card</title>
<link rel="stylesheet" href="https://fonts.googleapis.com/css2?family=Open+Sans:wght@400;600;700&display=swap">
<style>
  :root {
    --backdrop: #25262a;
    --card: #ffffff;
    --leaf-green: #7cbe3e;
    --earth-brown: #7a6a58;
    --text-grey: #7b7b7b;
    --faint-tint: #e9ece3;
    --card-shadow: rgba(0, 0, 0, 0.45);
  }
  * { box-sizing: border-box; margin: 0; padding: 0; }
  html, body {
    width: 1200px;
    height: 900px;
    overflow: hidden;
    background: var(--backdrop);
    font-family: "Open Sans", Arial, sans-serif;
  }
  .stage {
    position: relative;
    width: 1200px;
    height: 900px;
  }
  .card {
    position: absolute;
    width: 500px;
    height: 300px;
    background: var(--card);
    overflow: hidden;
    box-shadow: 0 8px 24px var(--card-shadow);
  }
  .card--front { left: 70px; top: 300px; }
  .card--back { left: 630px; top: 300px; }

  .brand {
    display: flex;
    align-items: center;
    gap: 12px;
  }
  .brand__dot {
    width: 46px;
    height: 46px;
    border-radius: 50%;
    background: var(--leaf-green);
    flex: none;
  }
  .brand__name {
    font-weight: 700;
    font-size: 30px;
    color: var(--leaf-green);
    letter-spacing: -0.3px;
    white-space: nowrap;
  }
  .card--front .brand {
    position: absolute;
    left: 0; right: 0; top: 0; bottom: 0;
    justify-content: center;
  }
  .card--back .brand {
    position: absolute;
    left: 30px;
    top: 34px;
  }
  .card--back .brand__dot { width: 38px; height: 38px; }
  .card--back .brand__name { font-size: 25px; }

  .backdrop-disc {
    position: absolute;
    right: -70px;
    top: -10px;
    width: 250px;
    height: 250px;
    border-radius: 50%;
    background: var(--faint-tint);
  }

  .person {
    position: absolute;
    left: 30px;
    top: 128px;
  }
  .person__name {
    font-weight: 600;
    font-size: 25px;
    color: var(--leaf-green);
    line-height: 1.1;
  }
  .person__role {
    font-size: 14px;
    color: var(--text-grey);
    margin-top: 2px;
  }

  .contacts {
    position: absolute;
    left: 30px;
    bottom: 40px;
    list-style: none;
  }
  .contacts li {
    display: flex;
    align-items: center;
    gap: 9px;
    font-size: 14px;
    line-height: 20px;
    color: var(--leaf-green);
  }
  .contacts svg {
    width: 11px;
    height: 11px;
    fill: none;
    stroke: var(--text-grey);
    stroke-width: 1.6;
    flex: none;
  }
  .accent-band {
    position: absolute;
    left: 0; right: 0; bottom: 0;
    height: 22px;
    background: var(--leaf-green);
  }
</style>
</head>
<body>
<main class="stage">
  <section class="card card--front" aria-label="Card front">
    <div class="brand">
      <span class="brand__dot"></span>
      <span class="brand__name">Meridale Gardening</span>
    </div>
  </section>

  <section class="card card--back" aria-label="Card back">
    <div class="backdrop-disc"></div>
    <div class="brand">
      <span class="brand__dot"></span>
      <span class="brand__name">Meridale Gardening</span>
    </div>
    <div class="person">
      <p class="person__name">Trevor Kalbrook</p>
      <p class="person__role">Horticulturalist</p>
    </div>
    <ul class="contacts">
      <li>
        <svg viewBox="0 0 12 12" aria-hidden="true"><path d="M3 1.5 L4.8 4 L3.8 5.2 Q5 7.5 6.8 8.2 L8 7.2 L10.5 9 L9.3 10.6 Q4 10 1.5 2.8 Z" fill="var(--text-grey)" stroke="none"/></svg>
        <span>0452739186</span>
      </li>
      <li>
        <svg viewBox="0 0 12 12" aria-hidden="true"><rect x="1" y="2.5" width="10" height="7"/><path d="M1 2.5 L6 6.5 L11 2.5"/></svg>
        <span>meridalegard@fernpost.com</span>
      </li>
      <li>
        <svg viewBox="0 0 12 12" aria-hidden="true"><circle cx="6" cy="6" r="4.8"/><path d="M1.2 6 H10.8 M6 1.2 Q3 6 6 10.8 M6 1.2 Q9 6 6 10.8"/></svg>
        <span>www.meridalegardening.com.au</span>
      </li>
    </ul>
    <div class="accent-band"></div>
  </section>
</main>
</body>
</html>
```